Harwick Electrical Business Card

create a simple but clear business card and letterhead - needs to be professional not too fancy and direct.

Target Market(s)

Home builders

Contact Information for Business Card

Information needed
Harwick Electrical Contracting
EC. No. 038275
Dario Pellegrin
Mobile 0427351186
dario@harwickelectrics.com.au

Requirements
Must have
• logo
• Harwick Electrical Contracting - H.E.D.
• EC. No. 038275
• Dario Pellegrin
• Mobile 0427351186
• dario@harwickelectrics.com.au
Nice to have
• black with white printing simple but clear
Should not have
• too much information
• no fancy writing

```html
<!DOCTYPE html>
<html lang="en">
<head>
<meta charset="utf-8">
<title>Harwick Electrical Contracting – Business Card</title>
<link rel="stylesheet" href="https://fonts.googleapis.com/css2?family=Arimo:wght@400&family=Lato:wght@400;900&display=swap">
<style>
  :root {
    --page: #e4e4e4;
    --ink: #1f1f1f;
    --card-dark: #262626;
    --card-light: #ffffff;
    --paper-text: #ffffff;
    --edge-band: #2a2a2a;
  }
  * { margin: 0; padding: 0; box-sizing: border-box; }
  html, body { width: 1200px; height: 900px; overflow: hidden; }
  body {
    background: var(--page);
    position: relative;
    font-family: "Lato", sans-serif;
  }
  .card {
    position: absolute;
    width: 700px;
    height: 400px;
    box-shadow: 0 8px 24px rgba(0,0,0,0.18);
  }
  .card--back {
    left: 310px; top: 40px;
    background: var(--card-dark);
    color: var(--paper-text);
  }
  .card--front {
    left: 190px; top: 470px;
    background: var(--card-light);
    color: var(--ink);
  }

  .brand {
    position: absolute;
    display: flex;
    align-items: center;
    gap: 18px;
  }
  .brand__dot {
    width: 78px; height: 78px;
    border-radius: 50%;
    background: currentColor;
    flex: none;
  }
  .brand__name {
    font-family: "Lato", sans-serif;
    font-weight: 900;
    line-height: 1.05;
    text-transform: uppercase;
  }
  .brand__name span { display: block; }
  .brand__name .brand__line1 { font-size: 40px; letter-spacing: 1px; }
  .brand__name .brand__line2 { font-size: 21px; letter-spacing: 0.5px; }

  .card--back .brand { left: 150px; top: 110px; }
  .card--back .website {
    position: absolute;
    left: 0; right: 0; top: 290px;
    text-align: center;
    font-size: 20px;
    letter-spacing: 2.5px;
  }

  .card--front .brand { left: 40px; top: 46px; }
  .card--front .brand__dot { width: 66px; height: 66px; }
  .card--front .brand__name .brand__line1 { font-size: 34px; }
  .card--front .brand__name .brand__line2 { font-size: 18px; }

  .edge-band {
    position: absolute;
    right: 0; top: 110px;
    width: 14px; height: 290px;
    background: var(--edge-band);
  }

  .contact {
    position: absolute;
    right: 60px; top: 150px;
    text-align: right;
  }
  .contact__name {
    font-family: "Arimo", sans-serif;
    font-size: 31px;
    margin-bottom: 10px;
  }
  .contact__line {
    font-size: 21px;
    line-height: 1.3;
  }
  .contact__row {
    display: flex;
    justify-content: flex-end;
    align-items: center;
    gap: 12px;
    font-size: 22px;
    line-height: 1.35;
  }
  .contact__row--first { margin-top: 10px; }
  .icon { width: 18px; height: 18px; flex: none; }
</style>
</head>
<body>

  <section class="card card--back" aria-label="Card back">
    <div class="brand">
      <div class="brand__dot"></div>
      <div class="brand__name">
        <span class="brand__line1">Harwick</span>
        <span class="brand__line2">Electrical Contracting</span>
      </div>
    </div>
    <p class="website">www.harwickelectrics.com.au</p>
  </section>

  <section class="card card--front" aria-label="Card front">
    <div class="brand">
      <div class="brand__dot"></div>
      <div class="brand__name">
        <span class="brand__line1">Harwick</span>
        <span class="brand__line2">Electrical Contracting</span>
      </div>
    </div>

    <div class="contact">
      <p class="contact__name">Dario Pellegrin</p>
      <p class="contact__line">Harwick Electrical Contracting</p>
      <p class="contact__line">EC. No. 038275</p>
      <p class="contact__row contact__row--first">
        0427 351186
        <svg class="icon" viewBox="0 0 18 18" aria-hidden="true">
          <rect x="4" y="1" width="10" height="16" rx="1.5" fill="none" stroke="#1f1f1f" stroke-width="1.5"/>
          <rect x="6" y="3.5" width="6" height="6" fill="#1f1f1f"/>
          <circle cx="9" cy="13.5" r="1.2" fill="#1f1f1f"/>
        </svg>
      </p>
      <p class="contact__row">
        dario@harwickelectrics.com.au
        <svg class="icon" viewBox="0 0 18 18" aria-hidden="true">
          <rect x="1" y="3.5" width="16" height="11" fill="#1f1f1f"/>
          <polyline points="1,3.5 9,10 17,3.5" fill="none" stroke="#ffffff" stroke-width="1.2"/>
        </svg>
      </p>
    </div>

    <div class="edge-band"></div>
  </section>

</body>
</html>
```